Book Cover for: TITLE Mend the Quiet Hours SUBTITLE For partners who would rather stay close

We need a full cover design for a book on relationships written by husband and wife team, Marla and Walter Dunmore, PhD. This book will offer hope for couples that are on the verge of breaking up but want to work things out and stay together. The theme is to teach couples about their own reactions to their partner, how moods affect a relationship, how to get creative to solving problems and how to have a good feeling towards your partner regardless of differences. This book is about hope. It is a positive look at relationships that feel hopeless.

Target Market(s)

Married or couples that are going through a difficult time and are considering splitting up due to, communication difficulties, addiction, affair. We imagine the book will appeal to women more than men but still want a cover that men would be comfortable picking up.

Colors

Designer to choose colors to be used in the design.

Requirements
Must have
• We want the cover to beautiful, intriguing, simple and uncomplicated. We don't want it overly busy, technical, or complex.
Nice to have
• MAYBE?? a broken heart being put back together.
Should not have
• No photo, no cartoon, no flowers, no couple (unless obscure and not gender specific).

```html
<!DOCTYPE html>
<html lang="en">
<head>
<meta charset="utf-8">
<title>Mend the Quiet Hours — Book Cover</title>
<link href="https://fonts.googleapis.com/css2?family=Cinzel:wght@400;600&family=Cormorant+Garamond:ital,wght@1,500&family=Great+Vibes&display=swap" rel="stylesheet">
<style>
  :root {
    --stage: #cfa68c;
    --paper: #f1f7fa;
    --ink: #0d0d0d;
    --heart-red: #e21d2a;
    --heart-deep: #c8141f;
  }
  * { margin: 0; padding: 0; box-sizing: border-box; }
  html, body {
    width: 1200px;
    height: 673px;
    overflow: hidden;
    background: var(--stage);
  }
  .cover {
    position: absolute;
    left: 376px;
    top: 0;
    width: 447px;
    height: 673px;
    background: var(--paper);
    color: var(--ink);
    overflow: hidden;
  }
  .subtitle {
    position: absolute;
    top: 38px;
    left: 0;
    width: 100%;
    text-align: center;
    font-family: "Cormorant Garamond", serif;
    font-style: italic;
    font-weight: 500;
    font-size: 19px;
    line-height: 21px;
    text-transform: uppercase;
    letter-spacing: 0.3px;
  }
  .title-top {
    position: absolute;
    top: 104px;
    left: 0;
    width: 100%;
    text-align: center;
    font-family: "Cinzel", serif;
    font-weight: 400;
    font-size: 58px;
    line-height: 62px;
    letter-spacing: 2px;
    text-transform: uppercase;
  }
  .rule {
    position: absolute;
    top: 194px;
    height: 2px;
    background: var(--ink);
  }
  .rule--left { left: 41px; width: 89px; clip-path: polygon(0 50%, 100% 0, 100% 100%); }
  .rule--right { left: 318px; width: 86px; clip-path: polygon(0 0, 100% 50%, 0 100%); }
  .title-bottom {
    position: absolute;
    top: 226px;
    left: 0;
    width: 100%;
    text-align: center;
    font-family: "Cinzel", serif;
    font-weight: 400;
    font-size: 104px;
    line-height: 104px;
    letter-spacing: -1px;
    text-transform: uppercase;
  }
  .title-script {
    position: absolute;
    top: 150px;
    left: 0;
    width: 100%;
    text-align: center;
    font-family: "Great Vibes", cursive;
    font-size: 104px;
    line-height: 104px;
    color: var(--heart-red);
    z-index: 2;
  }
  .heart-art {
    position: absolute;
    left: 104px;
    top: 337px;
    width: 249px;
    height: 222px;
    border-radius: 46% 46% 50% 50% / 40% 40% 60% 60%;
    background: radial-gradient(ellipse at 50% 45%, var(--heart-red) 0%, var(--heart-deep) 100%);
  }
  .authors {
    position: absolute;
    top: 590px;
    left: 0;
    width: 100%;
    text-align: center;
    font-family: "Cinzel", serif;
    font-weight: 600;
    font-size: 27px;
    line-height: 31px;
    letter-spacing: 0.5px;
    text-transform: uppercase;
  }
</style>
</head>
<body>
  <main class="cover">
    <p class="subtitle">For partners who<br>would rather stay close</p>
    <h1 class="title">
      <span class="title-top">Mend the</span>
      <span class="rule rule--left"></span>
      <span class="rule rule--right"></span>
      <span class="title-script">quiet</span>
      <span class="title-bottom">Hours</span>
    </h1>
    <div class="heart-art" role="img" aria-label="Red paper heart split by a crack, held together with a bandage strip"></div>
    <p class="authors">Marla and Walter<br>Dunmore, PhD</p>
  </main>
</body>
</html>
```